Business Card Design Coralgate Airflow Solutions

The Business will be centred around supply and installation of Ventilation for domestic homes and warehousing/workshops, and will be marketed as a Eco friendly means of reducing your carbon footprint and reducing energy consumption.Our suppliers will provide a range of products that will ventilate roof spaces and later will branch into to air transfer within homes for cooling and heating other rooms of the home etc.I would like to see colours that would be commensurate with the logo provided and yet not dominate the logo.Final design should convey a Diverse , professional but friendly service that will suit client needs

Target Market(s)

Domestic home owners and warehousing/workshop businesses

Industry/Entity Type

Business

Contact Information for Business Card

Company Name: Coralgate Airflow Solutions Pty Ltd, ABN: 42 817 359 264, Address: 27 Marrowfen Tulvanna W.A 6289, Email: dale@coralgateairflowsolutions.com.au, Mobile Number: 0461 852 309

Requirements
Nice to have
• A tract art that commensurate of the logo supplied
Should not have
• Font style that opposes logo design

```html
<!DOCTYPE html>
<html lang="en">
<head>
<meta charset="utf-8">
<title>Coralgate Airflow Solutions – Business Card</title>
<link href="https://fonts.googleapis.com/css2?family=Open+Sans:wght@400;600;700&display=swap" rel="stylesheet">
<style>
  :root {
    --green: #0bb04a;
    --brown: #561c1f;
    --white: #ffffff;
    --backdrop: #ececec;
  }
  * { margin: 0; padding: 0; box-sizing: border-box; }
  html, body {
    width: 1128px; height: 1200px; overflow: hidden;
    background: var(--backdrop);
    font-family: "Open Sans", Arial, sans-serif;
  }
  .sheet {
    width: 1128px; height: 1200px;
    display: flex; flex-direction: column; align-items: center;
    justify-content: space-evenly;
  }
  .card {
    position: relative;
    width: 960px; height: 552px;
    overflow: hidden;
    box-shadow: 0 2px 6px rgba(0,0,0,.15);
  }
  .card-front { background: var(--white); }
  .card-back { background: var(--green); }
  .card-art { position: absolute; inset: 0; width: 100%; height: 100%; }

  .brand-name {
    position: absolute;
    display: flex; align-items: center; gap: 16px;
    color: var(--brown);
    font-weight: 600;
    white-space: nowrap;
  }
  .brand-dot {
    width: 22px; height: 22px; border-radius: 50%;
    background: var(--green); flex: none;
  }
  .card-front .brand-name {
    left: 0; right: 0; top: 252px;
    justify-content: center;
    font-size: 48px;
  }
  .card-back .brand-name {
    right: 40px; top: 96px;
    font-size: 30px;
  }

  .company {
    position: absolute; left: 44px; top: 322px;
    color: var(--white);
  }
  .company-name { font-size: 34px; font-weight: 700; line-height: 1.1; }
  .company-abn { font-size: 27px; font-weight: 700; margin-left: 12px; margin-top: 6px; }

  .contact-list {
    position: absolute; left: 44px; top: 450px;
    list-style: none; color: var(--white);
  }
  .contact-item {
    display: flex; align-items: center; gap: 12px;
    height: 34px;
  }
  .contact-icon { width: 24px; height: 24px; flex: none; }
  .contact-phone { font-size: 26px; font-weight: 700; }
  .contact-email { font-size: 22px; font-weight: 400; }
  .contact-address { font-size: 24px; font-weight: 600; text-transform: uppercase; }
</style>
</head>
<body>
<main class="sheet">

  <section class="card card-front" aria-label="Business card front">
    <svg class="card-art" viewBox="0 0 960 552" aria-hidden="true">
      <rect x="0" y="0" width="960" height="88" fill="var(--green)"/>
      <path d="M0 452 Q480 482 960 454 Q480 494 0 452 Z" fill="var(--green)"/>
      <path d="M0 552 L0 534 Q480 414 960 534 L960 552 Z" fill="var(--green)"/>
    </svg>
    <div class="brand-name"><span class="brand-dot"></span>Coralgate Airflow Solutions</div>
  </section>

  <section class="card card-back" aria-label="Business card back">
    <svg class="card-art" viewBox="0 0 960 552" aria-hidden="true">
      <path d="M220 0 C420 90 700 268 960 296 L960 0 Z" fill="var(--brown)"/>
      <path d="M234 0 C432 82 700 250 960 272 L960 0 Z" fill="var(--green)"/>
      <path d="M250 0 C444 72 700 228 960 240 L960 0 Z" fill="var(--white)"/>
    </svg>

    <div class="brand-name"><span class="brand-dot"></span>Coralgate Airflow Solutions</div>

    <div class="company">
      <p class="company-name">Coralgate Airflow Solutions Pty Ltd.</p>
      <p class="company-abn">ABN: 42 817 359 264</p>
    </div>

    <ul class="contact-list">
      <li class="contact-item contact-phone">
        <svg class="contact-icon" viewBox="0 0 24 24" aria-hidden="true">
          <rect x="6" y="1" width="12" height="22" rx="2" fill="var(--white)"/>
          <rect x="8" y="4" width="8" height="11" fill="var(--green)"/>
          <circle cx="12" cy="19" r="1.6" fill="var(--green)"/>
        </svg>
        0461 852 309
      </li>
      <li class="contact-item contact-email">
        <svg class="contact-icon" viewBox="0 0 24 24" aria-hidden="true">
          <rect x="2" y="5" width="20" height="14" rx="1.5" fill="var(--white)"/>
          <path d="M3 6 L12 13 L21 6" fill="none" stroke="var(--green)" stroke-width="2"/>
        </svg>
        dale@coralgateairflowsolutions.com.au
      </li>
      <li class="contact-item contact-address">
        <svg class="contact-icon" viewBox="0 0 24 24" aria-hidden="true">
          <path d="M12 2 L23 12 L20 12 L20 22 L4 22 L4 12 L1 12 Z" fill="var(--white)"/>
          <rect x="10" y="15" width="4" height="7" fill="var(--green)"/>
        </svg>
        27 Marrowfen Tulvanna W.A 6289
      </li>
    </ul>
  </section>

</main>
</body>
</html>
```